Bag packaging design of sliced bread

The project is for design of line of sliced bread with different flavours. The brand of the bread will be "Valorina". The shape of the bread will be oval. The bread will be packed in a bag. I attach the layout of the bag. The bag will be closed with a plastic clip. I attach images of similar products. The idea is to have one main design and then each colour to be different type of bread like those in the images 2 and 5.

```html
<!DOCTYPE html>
<html lang="ro">
<head>
<meta charset="utf-8">
<title>Valorina – sliced bread bag range</title>
<link rel="stylesheet" href="https://fonts.googleapis.com/css2?family=Roboto+Condensed:wght@300;400;700&display=swap">
<style>
  :root {
    --canvas: #ffffff;
    --film: rgba(232, 236, 240, 0.55);
    --film-edge: rgba(190, 198, 206, 0.7);
    --crumb-light: #e9d2b4;
    --crumb: #d2ab82;
    --crust: #a9774d;
    --label-black: #121212;
    --tie-black: #0d0d0d;
    --ink-light: #f1ede6;
    --ink-muted: #bdb6aa;
    --mint: #6fd6c6;
    --mint-deep: #3fb3a3;
    --lime: #a7d24d;
    --lime-deep: #5e7a28;
    --sun: #f6dc3c;
    --sun-deep: #e0a92a;
    --text-font: "Roboto Condensed", "Arial Narrow", sans-serif;
  }
  * { box-sizing: border-box; margin: 0; padding: 0; }
  html, body {
    width: 1200px; height: 829px; overflow: hidden;
    background: var(--canvas);
    font-family: var(--text-font);
  }
  .range { position: relative; width: 1200px; height: 829px; }

  .pack { position: absolute; top: 30px; width: 270px; height: 760px; }
  .pack--sandwich { left: 165px; --accent: var(--mint); --accent-deep: var(--mint-deep); }
  .pack--brown    { left: 465px; --accent: var(--lime); --accent-deep: var(--lime-deep); }
  .pack--milk     { left: 765px; --accent: var(--sun);  --accent-deep: var(--sun-deep); }

  .pack__neck { position: absolute; left: 0; top: 0; width: 270px; height: 140px; }

  .pack__bag {
    position: absolute; top: 120px; left: 10px;
    width: 250px; height: 620px;
    border-radius: 115px / 80px;
    border: 1.5px solid var(--film-edge);
    overflow: hidden;
    background: var(--film);
  }
  .pack__bread {
    position: absolute; inset: 14px 12px;
    border-radius: 105px / 70px;
    background:
      repeating-linear-gradient(180deg, transparent 0 26px, rgba(169,119,77,0.28) 26px 28px),
      linear-gradient(90deg, var(--crust) 0%, var(--crumb) 14%, var(--crumb-light) 45%, var(--crumb) 85%, var(--crust) 100%);
    opacity: 0.85;
  }
  .pack__gloss {
    position: absolute; inset: 0;
    background: linear-gradient(90deg, rgba(255,255,255,0.55) 0%, rgba(255,255,255,0.08) 25%, rgba(255,255,255,0) 60%, rgba(255,255,255,0.35) 100%);
  }
  .pack__band {
    position: absolute; top: 0; bottom: 0; left: 72px; width: 78px;
    background: linear-gradient(180deg, var(--accent), var(--accent-deep) 50%, var(--accent));
    opacity: 0.9;
  }

  .label {
    position: absolute; left: 14px; top: 248px;
    width: 222px; height: 290px;
    border-radius: 50%;
    background: var(--label-black);
    border: 2px solid var(--accent);
    box-shadow: inset 0 0 0 5px var(--label-black), inset 0 0 0 6px rgba(255,255,255,0.12);
    overflow: hidden;
  }
  .label__wheat {
    position: absolute; left: 70px; top: 40px; width: 80px; height: 210px;
    border-radius: 50%;
    background: radial-gradient(ellipse at center, rgba(210,205,195,0.22), rgba(210,205,195,0) 70%);
  }
  .label__content {
    position: absolute; left: 50%; top: 50%;
    width: 270px; height: 190px;
    transform: translate(-50%, -50%) rotate(-90deg);
    display: flex; flex-direction: column; align-items: center;
    padding-top: 6px;
  }
  .label__badges { display: flex; justify-content: space-between; width: 190px; height: 34px; }
  .badge { width: 30px; height: 30px; border-radius: 50%; border: 1.5px solid var(--ink-muted); }
  .badge--filled { background: var(--ink-light); border-color: var(--ink-light); }

  .label__brand {
    margin-top: 4px;
    font-weight: 400; font-size: 52px; line-height: 1;
    color: var(--ink-light); letter-spacing: 1px;
  }
  .label__subtitle {
    margin-top: 6px;
    font-weight: 300; font-size: 15px; color: var(--ink-light); letter-spacing: 0.5px;
  }
  .label__variant { margin-top: 8px; display: flex; flex-direction: column; align-items: center; gap: 4px; }
  .variant__name {
    background: var(--accent); color: var(--label-black);
    font-weight: 400; font-size: 14px; letter-spacing: 3px;
    padding: 2px 8px; text-transform: uppercase;
  }
  .variant__cut {
    background: var(--ink-light); color: var(--label-black);
    font-weight: 700; font-size: 13px; letter-spacing: 1.5px;
    padding: 1px 8px; text-transform: uppercase;
  }
</style>
</head>
<body>
<main class="range">

  <article class="pack pack--sandwich">
    <svg class="pack__neck" viewBox="0 0 270 140" aria-hidden="true">
      <path d="M70 140 Q110 100 118 60 L152 60 Q160 100 200 140 Z" fill="rgba(225,230,235,0.8)" stroke="rgba(190,198,206,0.8)"/>
      <path d="M112 70 L108 20 Q140 0 180 10 Q200 18 190 40 L160 70 Z" fill="var(--tie-black)"/>
      <rect x="114" y="66" width="42" height="10" rx="3" fill="var(--tie-black)"/>
    </svg>
    <div class="pack__bag">
      <div class="pack__bread" role="img" aria-label="Sliced sandwich bread seen through the clear film"></div>
      <div class="pack__band" role="img" aria-label="Mint diamond check pattern band"></div>
      <div class="pack__gloss"></div>
      <div class="label">
        <div class="label__wheat" role="img" aria-label="Line drawing of wheat ears"></div>
        <div class="label__content">
          <div class="label__badges"><span class="badge badge--filled"></span><span class="badge"></span><span class="badge"></span></div>
          <h2 class="label__brand">Valorina</h2>
          <p class="label__subtitle">Cu malț de secară</p>
          <div class="label__variant"><span class="variant__name">Sandwich bread</span><span class="variant__cut">Sliced</span></div>
        </div>
      </div>
    </div>
  </article>

  <article class="pack pack--brown">
    <svg class="pack__neck" viewBox="0 0 270 140" aria-hidden="true">
      <path d="M70 140 Q110 100 118 60 L152 60 Q160 100 200 140 Z" fill="rgba(225,230,235,0.8)" stroke="rgba(190,198,206,0.8)"/>
      <path d="M112 70 L100 22 Q130 0 170 12 Q200 22 185 45 L160 70 Z" fill="var(--tie-black)"/>
      <rect x="114" y="66" width="42" height="10" rx="3" fill="var(--tie-black)"/>
    </svg>
    <div class="pack__bag">
      <div class="pack__bread" role="img" aria-label="Sliced brown bread seen through the clear film"></div>
      <div class="pack__band" role="img" aria-label="Green diamond check pattern band"></div>
      <div class="pack__gloss"></div>
      <div class="label">
        <div class="label__wheat" role="img" aria-label="Line drawing of wheat ears"></div>
        <div class="label__content">
          <div class="label__badges"><span class="badge badge--filled"></span><span class="badge"></span><span class="badge"></span></div>
          <h2 class="label__brand">Valorina</h2>
          <p class="label__subtitle">Cu malț de secară</p>
          <div class="label__variant"><span class="variant__name">Brown bread</span><span class="variant__cut">Sliced</span></div>
        </div>
      </div>
    </div>
  </article>

  <article class="pack pack--milk">
    <svg class="pack__neck" viewBox="0 0 270 140" aria-hidden="true">
      <path d="M70 140 Q110 100 118 60 L152 60 Q160 100 200 140 Z" fill="rgba(225,230,235,0.8)" stroke="rgba(190,198,206,0.8)"/>
      <path d="M112 70 L104 18 Q140 2 178 14 Q196 24 186 44 L160 70 Z" fill="var(--tie-black)"/>
      <rect x="114" y="66" width="42" height="10" rx="3" fill="var(--tie-black)"/>
    </svg>
    <div class="pack__bag">
      <div class="pack__bread" role="img" aria-label="Milk bread loaf seen through the clear film"></div>
      <div class="pack__band" role="img" aria-label="Yellow diamond check pattern band"></div>
      <div class="pack__gloss"></div>
      <div class="label">
        <div class="label__wheat" role="img" aria-label="Line drawing of wheat ears"></div>
        <div class="label__content">
          <div class="label__badges"><span class="badge badge--filled"></span><span class="badge"></span><span class="badge"></span></div>
          <h2 class="label__brand">Valorina</h2>
          <p class="label__subtitle">Cu malț de secară</p>
          <div class="label__variant"><span class="variant__name">Milk bread</span><span class="variant__cut">Loaf</span></div>
        </div>
      </div>
    </div>
  </article>

</main>
</body>
</html>
```